Mosquito and outdoor pest management

The uploaded logo must be integrated as the main theme of the card. I would like it to be modern and eye catching. Maybe some backround images or light silver metallic background.
Space enough at the base for contact info to be put in- phone numbers,emails,names,website.
Space on the back for short blog and lines for hand writing..calling card.
Target Market(s)
Commercial- golf courses, schools, outdoor function properties, pre event treatments.
Residential- retirement villages, townhome complexes and general houses
Industry/Entity Type
Management

```html
<!DOCTYPE html>
<html lang="en">
<head>
<meta charset="utf-8">
<title>Norwood Biteguard – Business Card</title>
<link rel="stylesheet" href="https://fonts.googleapis.com/css2?family=Noto+Serif:wght@400;700&family=Open+Sans:wght@400&display=swap">
<style>
  :root {
    --backdrop: #c6c6c6;
    --card-black: #050505;
    --card-white: #ffffff;
    --brand-red: #e3222c;
    --ink: #111111;
    --text-light: #f2f2f2;
  }
  * { box-sizing: border-box; margin: 0; padding: 0; }
  html, body { width: 992px; height: 1200px; overflow: hidden; }
  body { background: var(--backdrop); position: relative; font-family: "Open Sans", Arial, sans-serif; }

  .card { position: absolute; left: 99px; width: 807px; height: 461px; background: var(--card-black); overflow: hidden; }
  .card--front { top: 104px; }
  .card--back { top: 624px; }

  .front-header { position: absolute; left: 0; top: 0; width: 100%; height: 241px; background: var(--card-white); }
  .front-rule { position: absolute; left: 0; top: 241px; width: 100%; height: 10px; background: var(--brand-red); }

  .brand { position: absolute; left: 66px; top: 88px; display: flex; align-items: center; gap: 26px; }
  .brand-name { font-family: "Open Sans", Arial, sans-serif; font-weight: 400; font-size: 56px; line-height: 1; color: var(--ink); white-space: nowrap; }
  .brand-dot { width: 44px; height: 44px; border-radius: 50%; background: var(--brand-red); flex: none; }

  .holder-name { position: absolute; left: 66px; top: 326px; font-family: "Noto Serif", Georgia, serif; font-weight: 700; font-size: 40px; color: var(--brand-red); }
  .contact-divider { position: absolute; left: 353px; top: 283px; width: 2px; height: 141px; background: var(--text-light); }

  .contact-list { position: absolute; left: 395px; top: 292px; list-style: none; }
  .contact-item { display: flex; align-items: center; height: 41.5px; color: var(--text-light); font-size: 25px; white-space: nowrap; }
  .contact-icon { width: 17px; height: 17px; margin-right: 21px; flex: none; }

  .service-group { position: absolute; left: 100px; }
  .service-group--commercial { top: 64px; }
  .service-group--residential { top: 276px; }
  .service-heading { display: flex; align-items: center; width: 393px; border-bottom: 2px solid var(--brand-red); }
  .service-group--residential .service-heading { width: 385px; }
  .service-bullet { width: 14px; height: 14px; border-radius: 50%; background: var(--brand-red); margin: 0 30px 0 18px; }
  .service-title { font-family: "Noto Serif", Georgia, serif; font-weight: 400; font-size: 36px; line-height: 1.05; color: var(--brand-red); }
  .service-list { list-style: none; margin-left: 63px; margin-top: 16px; color: var(--text-light); font-size: 25px; }
  .service-group--residential .service-list { margin-top: 8px; }
  .service-list li { height: 35px; line-height: 35px; }
</style>
</head>
<body>
  <section class="card card--front" aria-label="Card front">
    <div class="front-header">
      <div class="brand">
        <div class="brand-name">Norwood Biteguard</div>
        <div class="brand-dot"></div>
      </div>
    </div>
    <div class="front-rule"></div>

    <div class="holder-name">Daniel Hart</div>
    <div class="contact-divider"></div>
    <ul class="contact-list">
      <li class="contact-item">
        <svg class="contact-icon" viewBox="0 0 16 16" aria-hidden="true"><rect width="16" height="16" fill="#e3222c"/><path d="M5 3.5l2 2-1.2 1.3c.6 1.4 1.7 2.5 3.1 3.1L10.2 8.7l2 2-1.4 1.8C7 12.2 3.8 9 3.5 5z" fill="#050505"/></svg>
        061 2345 7788
      </li>
      <li class="contact-item">
        <svg class="contact-icon" viewBox="0 0 16 16" aria-hidden="true"><rect width="16" height="16" fill="#e3222c"/><circle cx="8" cy="8" r="4.8" fill="none" stroke="#050505" stroke-width="1.3"/><path d="M3.2 8h9.6M8 3.2c-2.2 2.6-2.2 7 0 9.6M8 3.2c2.2 2.6 2.2 7 0 9.6" fill="none" stroke="#050505" stroke-width="1"/></svg>
        www.norwoodbiteguard.com
      </li>
      <li class="contact-item">
        <svg class="contact-icon" viewBox="0 0 16 16" aria-hidden="true"><rect width="16" height="16" fill="#e3222c"/><rect x="3" y="4.5" width="10" height="7" fill="none" stroke="#050505" stroke-width="1.2"/><path d="M3 4.5l5 4 5-4" fill="none" stroke="#050505" stroke-width="1.2"/></svg>
        hello@norwoodbiteguard.com
      </li>
    </ul>
  </section>

  <section class="card card--back" aria-label="Card back">
    <div class="service-group service-group--commercial">
      <div class="service-heading"><span class="service-bullet"></span><h2 class="service-title">Commercial</h2></div>
      <ul class="service-list">
        <li>schools</li>
        <li>golf courses</li>
        <li>pre event treatments</li>
        <li>outdoor function properties</li>
      </ul>
    </div>
    <div class="service-group service-group--residential">
      <div class="service-heading"><span class="service-bullet"></span><h2 class="service-title">Residential</h2></div>
      <ul class="service-list">
        <li>retirement villages</li>
        <li>townhome complexes and general houses</li>
      </ul>
    </div>
  </section>
</body>
</html>
```